Stem cell injections patient brochure

i need a patient brochure for stem cell injections

What started out as a controversial treatment option has turned out to be one of the most unique solutions when it comes to treating joint pain and other health conditions that require the rejuvenation or replacement of certain types of tissues. Individuals who have trouble with their joints due to damage to the bone and cartilage are eager to find solutions that do not involve surgery. Stem cell therapy and the use of amniotic fluids offer solutions that will allow them to begin the healing process and begin to reclaim their lives. Stem cells and the use of platelet rich plasma go hand in hand in helping to regenerate and restore joint structure and function allowing the person to regain their mobility without fear of creating more discomfort.

Uncovering the Benefits of Stem Cells

The study of stem cells has uncovered a myriad of benefits ranging from the relief of migraines to the restoration and rejuvenation of various joints throughout the body. Stem cells are harvested from the patient allowing for a more complete healing in which the body's own tools are given a boost to begin the rejuvenation process. Because the stem cells are drawn from the person's own body, there is less risk of rejection and the body will begin to restore itself much faster than if foreign cells were used. When it comes to the regeneration of tissues in the joints, stem cell therapy offers a unique approach that allows the body to use its own resources in the healing process. Stem cell therapy takes an existing process and gives it a dramatic boost that basically pushes the process into overdrive, regenerating damaged tissue and sustaining the healing response. One thing that many people like about the procedure is that the matrix used in the injections is made from stem cells, growth factors and platelets that are harvested from their own body. No foreign substances are used and the healing process that results is much more efficient and complete. The body is given exactly what it needs to heal itself on its own terms without toxic chemicals or invasive procedures that takes weeks or months to heal.

A Unique Treatment Solution

Stem cells offer treatment options and solutions that were unheard of as little as three decades ago. By injecting a matrix made from the body's own “blank” cells, the body is able to regenerate new, healthier tissues that grow and take the place of damaged tissues. Along with the blank, stem cells, certain growth factors are also harvested and added to the mix. Because of how stem cells are formed, they can begin to assume the DNA of almost any type of cell. This allows them to grow into whatever type of cell is needed, hastening the healing process by rebuilding stronger and healthier tissue. The body has been given the tools it needs to heal itself but it often has trouble setting the processes in motion. Stem cell therapy gives the body the boost it needs by flooding the area with the stem cells that can actually elicit a healing response and trigger the start of the process.

Where Do Stem Cells Come From?

Stem cells are no longer drawn from outside sources to be used in joint rejuvenation procedures. The body has an unlimited supply of stem cells that it uses on a regular basis as a way of replacing cells that mature and die off. Doctors have found ways to harvest those cells, as well as growth factors that help to hasten the healing process. Stem cells can be found throughout the entire body. They are produced in the bones, the blood, liver, brain, heart, and soft tissues. They can be found almost everywhere simply because they are the building blocks the body uses to maintain its structure. Because the body continually produces them, they can be harvested from almost any area at any time without fear of damaging existing tissues or disrupting other processes in the body.

What Types of Tissues Will Stem Cells Restore

Stems cells can be used to regenerate almost any type of tissue, including cartilage and bone. Most people who look to stem cell therapy, do so in the hopes that it will relieve their joint pain and allow the joint to function properly. Stem cells do have the capability of regenerating many different types of tissues, but their rate of effectiveness will be determined by existing factors, such as spurring, severe degeneration, and the presence of health conditions such as osteo- or rheumatoid arthritis. Each person's case is unique. The goal of the procedure is to regenerate the damaged tissues and reduce pain and discomfort. While the tissues may be regenerated and function partially restored, it may not provide enough of a change to completely eliminate all of the patient's pain or discomfort.

Stem Cell Treatment Options for Joints

Stem cell treatment options can be beneficial in many ways. They are fairly non-invasive in comparison to other types of procedures. The only part of the procedure that is termed as invasive would be the use of the needle to inject the matrix into the damaged area of the joint. There is practically no down-time and the patient can begin to resume their normal, day-to-day activities within a few hours after the procedure. While it may take a few weeks to begin to notice verifiable results, the addition of a platelet rich plasma injection a few weeks after the initial procedure will help to keep the healing process on track. When it comes to stem cell treatment options for knees and other joints, the procedure offers a unique solution that allows the body the opportunity to heal itself without harsh or extremely invasive procedures.

Is the Procedure Effective?

It has been proven that stem cells are capable of regenerating different types of tissues. The procedure's effectiveness, however, will be based on several factors. First and foremost, the extent of damage caused by the injury or disease will determine how effective the procedure will be. If the damage is extensive, the use of stem cells and platelet rich plasma injections may be beneficial, but it will not relieve all of the patient's pain and discomfort. The reason for this is that the damage may extend far beyond the cartilage and structural tissues. Nerves may be damaged or scar tissue may be present that limits how the bone and cartilage are able to heal. The patient's overall health will also play a vital role. Proper circulation and an abundance of oxygen and nutrients supplied by the bloodstream are imperative if the body's healing responses are expected to regenerate and restore the tissues. The person's willingness to follow the doctor's orders and maintain proper nutrition and sufficient amounts of physical therapy that is needed to strengthen the area are also important factors. In the first one or two months, patient will begin to notice less pain and discomfort. It can take up to six months or longer for the function to improve. The process will be gradual and will continue to improve over time.

Will More Injections be Needed in the Future?

In most cases, only one stem cell injection is used. To be effective, platelet rich plasma injections are included with the procedure so the stem cells continue to receive the nutrient's they need to continue the healing process. Platelet rich plasma is a matrix made up of approximately three times the number of platelets that are normally found in the blood. To make the PRP matrix, blood is drawn from the patients arm and concentrated to create a platelet rich solution that, when injected into an injured area, floods it with platelets that provide an abundance of nutrients that help to maintain the forward progress of the healing response. With one stem cell injection and one platelet rich plasma injection, spaced out over a period of three to four weeks, the patient will receive the maximum benefits from both procedures. Protocols can be adjusted if the person receiving the treatment is unavailable or needs to have the injections closer together.

How Do I Know if I Will Benefit From the Procedure?

Stem cell therapy is often considered for patients who have not responded well to other forms of treatment, especially for osteoarthritis. Individuals who have osteoarthritis may find it difficult to move the knee or other joint. They may also be experiencing reduced range of motion and flexibility which makes physical therapy difficult, not to mention, extremely painful. The longer the patient experiences impaired mobility, the harder it will be for them to remain active. Stem cell therapy may also be an effective option for individuals who would rather not go through the experience of a partial or total knee replacement procedure.

Individuals who have trouble with tendonitis caused by repetitive motions or movements due to a sport they participate in or as part of their work-related duties may be able to find the relief they seek by receiving stem cell and platelet rich plasma injections in the affected joints. Repetitive motions can damage both bone and cartilage causing inflammation and pain in and around the area of the joint. Over time, the pain and inflammation can become so severe that regular movement is difficult. Stem cell therapy can help to restore proper function by regenerating the damaged cartilage and tissues, much like it works within the knee joint. As the injured tissues begin to heal, the inflammation begins to decrease and the person will begin to experience greater range of motion and flexibility. Although stem cell injections may not completely correct the problem, it will help to reduce the pain and discomfort allowing the person freedom of movement and the ability to exercise the area and regain a portion of the strength that was lost.

Common Contraindications

Just like any other healthcare procedure, stem cell therapy does have several contraindications and is inadvisable for patients with specific health conditions. Individuals who have any type of blood borne cancer or have had cancer are normally encourage not to attempt a stem cell procedure. Leukemia and lymphoma are two cancers that are spread through the blood and can have a devastating impact on the body. Patients who are prone to any type of infection or have a depressed immune system should also avoid this type of procedure. The use of Velbrisol can also have a devastating impact on how the procedure works. Patients who use the drug on a regular basis are not good candidates for this type of procedure. Individuals who have chronic, recurring medical conditions that affect their general health and the body's ability to heal are also not good candidates.

Potential Risk Factors

Stem cell therapy has relatively few risks. The bone marrow cells are harvested from the patient's own tissues so there is minimal risk of rejection. The harvesting process may be somewhat uncomfortable but the doctor can offer medications to help alleviate any pain or discomfort. The cells are concentrated, separating the stem cells from other types of cells. Growth factors within the blood are allowed to remain in tact as a sort of booster that helps to kick start the process into motion. A mixture of highly concentrated stem cells and growth factors is created and injected directly into the affected area of the joint. Any injection will result in minimal amounts of pain. Doctors may offer a mild local anesthetic or they may prescribe a pain medication that can be taken after the procedure is over. Because the procedure is non-invasive, there is very little risk of infection and the healing time is relatively fast. The patient may experience mild pain and swelling near the injection site for the first few days after the procedure, but this will dissipate rather quickly allowing the person to return to their daily activities within a few hours.

The Procedure Itself

How Do I Prepare for the Procedure?

There is very little preparation needed before a stem cell injection procedure. Doctors recommend no anti-inflammatory medications for at least seven to ten days prior to the procedure. It is important to drink plenty of fluids prior to the procedure and make sure you are well rested and able to follow all of the doctor's requests once the procedure is underway. During your initial visit, the doctor will ask if you are taking any medications, such as Pondrexa or Velbrisol. If you are, the doctor will need to know so that he can tell you when to discontinue the medication prior to the procedure being performed. The day of the procedure make sure you have someone who can take you home and look after you for the first few hours after the procedure. You will need to make arrangements so that you can rest once you arrive home. Do not try and over do it or exceed your personal limitations. Even though this is not a surgical procedure, the doctor may recommend not eating for a few hours prior to the procedure to prevent nausea and an upset stomach while you are receiving the treatment.

What Happens When I Arrive?

The morning of the procedure make sure you are well rested and wearing comfortable clothes, You will be checked in and taken back to a room where the procedure will be performed. The nurse will prep the knee (or other joint) and make sure all of the tools are available for the doctor to use. The doctor will begin the harvesting process, which involves drawing blood and stem cells from the marrow of one of your bones. You will be allowed to rest while the matrix is being created. Once the stem cell solution has been created, the doctor will identify the area where the injection needs to be placed. The solution will then be injected into the joint.

What Are My Limitations After the Procedure?

Stem cell procedures do not produce immediate results. Although they will provide significant improvement when it comes to managing the patient's pain, the stem cells will not stimulate the growth of new cartilage over night. It can take anywhere from three to six months or longer for the patient to begin to experience noticeable results. The results may take even longer if the person has other health conditions that affect their body's ability to heal itself. Once the pain begins to subside, the patient should experience renewed mobility and range of motion that allow them to increase their flexibility and begin to exercise, even if only in modest amounts. The more the person moves the knees, strength will be improved. The more movement, the stronger the joint. As the healing process continues and more cartilage is regenerated, the fewer limitations the patient will experience.

Stem cell therapy is not a quick fix. The benefits of giving the body what it needs to restore itself and heal on its own without extensive surgery or potent medications offers many benefits. The lack of risk improves the chances of a more complete healing and allows the body to recover in a natural way that is more efficient and productive than if a surgery or other invasive procedure had been performed. The person's overall general health will determine the rate at which a person heals. Encouraging proper lifestyle habits, proper nutrition, adequate amounts of fluids and regular exercise will increase the patient's ability to heal faster and more effectively than someone who lives a sedentary lifestyle.

Talk to Your Doctor

Individuals who are experiencing knee or joint pain for any reason should consult with their doctor and ask whether or not stem cell therapy is right for them. Individuals who suffer from osteoarthritis and other types of degenerative bone condition may benefit substantially from a stem cell therapy procedure. Athletes who have repeatedly stressed or injured their joints may also be good candidates for this type of procedure. Common athletic injuries such as tendonitis can be effectively treated with a combination of stem cell therapy and platelet rich plasma injections. Repeated motion injuries like swimmer's shoulder, pitcher's elbow and carpal tunnel syndrome can be treated with stem cell injections when other treatment options begin to fail to produce sufficient relief. With these types of injuries, the regeneration of the tissues and cartilage not only significantly reduce the pain and discomfort a person feels when performing certain tasks, it also allows the person to regain the majority of their range of motion they may have otherwise lost.

It is important to remember that most insurance companies list this as an elective procedure so it is not normally covered under your health insurance. While it is recognized as an effective treatment by some, the protocols and benefits are still being researched. Studies are still being performed to provide accurate information on how effective the treatment is when used to treat specific types of injuries or illnesses. Until a consensus is reached and the NMB approves the procedure along with a list of conditions that it is capable of treating, insurance companies will not include coverage for this type of procedure in their health care policies.

If you have any questions or concerns about the cost of the procedure, how it is performed, the benefits, the risks, and whether or not there are any concerns or implications you need to be aware of, talk to your doctor. He will be able to offer advice and answer any of the questions you may have concerning the procedure. Your general health and lifestyle will determine whether or not the treatment is suitable for the issues you are having with your knees or other joints. Before you make the decision on whether or not to have the stem cell procedure performed, make sure you have all of the information you need to make a knowledgeable choice. Giving the body the tools it needs to heal itself using its own healing responses is beneficial in many ways, but it may not be the right option for you. Talk to your doctor and weigh both pros and cons before making your decision.

ient brochure trifold that explains stem cell injections

Target Market(s)

patient brochure

Industry/Entity Type

Health Care

Requirements
Must have
• dna pictures
• large trifold brochure
Nice to have
• stem cell pictures and injections

```html
<!DOCTYPE html>
<html lang="en">
<head>
<meta charset="utf-8">
<title>Stem Cell Injections – Patient Brochure</title>
<link rel="stylesheet" href="https://fonts.googleapis.com/css2?family=Lato:wght@400;700;900&display=swap">
<style>
  :root {
    --brand-blue: #0b5597;
    --footer-blue: #0a4e8f;
    --accent-orange: #f6aa3c;
    --logo-blue: #2f7fd0;
    --ink-dark: #1a1a1a;
    --white: #ffffff;
  }
  * { box-sizing: border-box; margin: 0; padding: 0; }
  html, body { width: 848px; height: 1200px; overflow: hidden; }
  body {
    font-family: "Lato", Arial, sans-serif;
    background: var(--white);
  }
  .brochure-page {
    width: 848px;
    height: 1200px;
    display: flex;
    flex-direction: column;
  }
  .content-panel {
    background: var(--brand-blue);
    color: var(--white);
    height: 1002px;
    padding: 28px 30px 0;
  }
  .section-title {
    font-weight: 700;
    font-size: 22.5px;
    text-align: center;
    text-transform: uppercase;
    letter-spacing: 0.1px;
    line-height: 28px;
    margin-bottom: 6px;
  }
  .section-title + .body-copy { margin-top: 0; }
  .body-copy {
    font-size: 15.6px;
    line-height: 20.8px;
    text-align: justify;
    text-align-last: center;
    margin-bottom: 10px;
  }
  .section-title.second { margin-top: 16px; }
  .brand-area {
    height: 97px;
    display: flex;
    flex-direction: column;
    align-items: center;
    justify-content: center;
    gap: 4px;
  }
  .brand-mark { width: 54px; height: 54px; }
  .brand-name {
    font-size: 24px;
    font-weight: 400;
    color: var(--ink-dark);
    line-height: 26px;
  }
  .contact-bar {
    background: var(--footer-blue);
    color: var(--white);
    height: 53px;
    display: flex;
    align-items: center;
    justify-content: center;
    font-size: 18.5px;
    font-weight: 700;
  }
  .contact-bar .divider { margin: 0 30px; font-weight: 400; }
  .web-bar {
    background: var(--accent-orange);
    color: var(--ink-dark);
    height: 48px;
    display: flex;
    align-items: center;
    justify-content: center;
    font-size: 18px;
    letter-spacing: 3.2px;
  }
</style>
</head>
<body>
<main class="brochure-page">
  <section class="content-panel">
    <h2 class="section-title">What are my limitations after the procedure?</h2>
    <p class="body-copy">Stem cell procedures do not produce immediate results. Although they will provide significant improvement when it comes to managing the patient's pain, the stem cells will not stimulate the growth of new cartilage over night. It can take anywhere from three to six months or longer for the patient to begin to experience noticeable results. The results may take even longer if the person has other health conditions that affect their body's ability to heal itself. Once the pain begins to subside, the patient should experience renewed mobility and range of motion that allow them to increase their flexibility and begin to exercise, even if only in modest amounts. The more the person moves the knees, strength will be improved. The more movement, the stronger the joint. As the healing process continues and more cartilage is regenerated, the fewer limitations the patient will experience.</p>
    <p class="body-copy">Stem cell therapy is not a quick fix. The benefits of giving the body what it needs to restore itself and heal on its own without extensive surgery or potent medications offers many benefits. The lack of risk improves the chances of a more complete healing and allows the body to recover in a natural way that is more efficient and productive than if a surgery or other invasive procedure had been performed. The person's overall general health will determine the rate at which a person heals. Encouraging proper lifestyle habits, proper nutrition, adequate amounts of fluids and regular exercise will increase the patient's ability to heal faster and more effectively than someone who lives a sedentary lifestyle.</p>

    <h2 class="section-title second">Talk to your doctor</h2>
    <p class="body-copy">Individuals who are experiencing knee or joint pain for any reason should consult with their doctor and ask whether or not stem cell therapy is right for them. Individuals who suffer from osteoarthritis and other types of degenerative bone condition may benefit substantially from a stem cell therapy procedure. Athletes who have repeatedly stressed or injured their joints may also be good candidates for this type of procedure. Common athletic injuries such as tendonitis can be effectively treated with a combination of stem cell therapy and platelet rich plasma injections. Repeated motion injuries like swimmer's shoulder, pitcher's elbow and carpal tunnel syndrome can be treated with stem cell injections when other treatment options begin to fail to produce sufficient relief. With these types of injuries, the regeneration of the tissues and cartilage not only significantly reduce the pain and discomfort a person feels when performing certain tasks, it also allows the person to regain the majority of their range of motion they may have otherwise lost.</p>
    <p class="body-copy">It is important to remember that most insurance companies list this as an elective procedure so it is not normally covered under your health insurance. While it is recognized as an effective treatment by some, the protocols and benefits are still being researched. Studies are still being performed to provide accurate information on how effective the treatment is when used to treat specific types of injuries or illnesses. Until a consensus is reached and the NMB approves the procedure along with a list of conditions that it is capable of treating, insurance companies will not include coverage for this type of procedure in their health care policies.</p>
    <p class="body-copy">If you have any questions or concerns about the cost of the procedure, how it is performed, the benefits, the risks, and whether or not there are any concerns or implications you need to be aware of, talk to your doctor. He will be able to offer advice and answer any of the questions you may have concerning the procedure. Your general health and lifestyle will determine whether or not the treatment is suitable for the issues you are having with your knees or other joints. Before you make the decision on whether or not to have the stem cell procedure performed, make sure you have all of the information you need to make a knowledgeable choice. Giving the body the tools it needs to heal itself using its own healing responses is beneficial in many ways, but it may not be the right option for you. Talk to your doctor and weigh both pros and cons before making your decision.</p>
  </section>

  <section class="brand-area">
    <svg class="brand-mark" viewBox="0 0 54 54" aria-hidden="true">
      <circle cx="27" cy="27" r="26" fill="var(--logo-blue)"/>
    </svg>
    <div class="brand-name">LOGO TEXT</div>
  </section>

  <footer>
    <div class="contact-bar">
      <span>0000 111 222</span><span class="divider">|</span>
      <span>Your Address Here</span><span class="divider">|</span>
      <span>youremail@here.com</span>
    </div>
    <div class="web-bar">www.yourwebaddresshere.com</div>
  </footer>
</main>
</body>
</html>
```